Website for business consultancy - bright and happy feel needed

I need a website with 3/4 pages. I want the first page designed first and the rest will be easy. I need some pictures but none with corporate looking people. I need links to chatterbox and careerweb. I need a contact form. I have samples of websites i like, fonts i like and I need a small logo also. I like simple, clean lines and I want a bright, happy and feminine feel. My audience are small businesses so I don't want them intimidated by new much of a corporate feel.
Updates

Project Deadline Extended Reason: I have not received a design that reflects what I believe the brief to be, therefore I am extending the deadline and increasing the amount to be paid. Added Thursday, October 13, 2016

Target Market(s)

Small medium size businesses who want to grow and need that help but they cannot afford a full time financial director.

Industry/Entity Type

Business Consultant

Number of Pages Required

4 page

Font styles to use
Other font styles liked:
• i can attach images

Colors
fcf0f6
e667a6
85cae6
ffffff
fbee3e

Requirements
Must have
• Link to chatterbox and career web
• Contact form linked to my email
• Pictures - full width images where required
• Colour
• Mobile ready
• Soft feminine feel to it
• I dont want it to look like a corporate business consultancy - much more marketing or interior deign feel
Nice to have
• I would like the 3 services I have in 3 boxes that you click and takes you to a place with more information on the service.
• pictures thinking outside of the box
• Can be wordpress if need be
Should not have
• pictures with too much of a corporate feel
• No pictures of coporate people at all
• i like the following websites
• www.pebblordo.co.uk and others that are attached in the documents with a feminine feel to them

```html
<!DOCTYPE html>
<html lang="en">
<head>
<meta charset="utf-8">
<title>Maren Holt Consulting</title>
<link href="https://fonts.googleapis.com/css2?family=Arimo:wght@400;700&family=Lato:wght@400&family=Tinos:wght@400;700&display=swap" rel="stylesheet">
<style>
  :root{
    --blush:#fcf0f6;
    --pink:#e667a6;
    --pink-deep:#c94b8a;
    --sky:#85cae6;
    --sunny:#fbee3e;
    --white:#ffffff;
    --plum:#4a3340;
    --plum-soft:#6d5562;
    --field-text:#5a4a53;
    --rule:rgba(230,103,166,.55);
  }
  *{box-sizing:border-box;margin:0;padding:0}
  html,body{width:1200px;height:585px;overflow:hidden;background:var(--blush)}
  body{position:relative;font-family:"Arimo",Arial,sans-serif;color:var(--plum)}

  .hero-backdrop{position:absolute;left:0;top:112px;width:1200px;height:429px;
    background:
      radial-gradient(ellipse 480px 220px at 520px 150px, rgba(255,255,255,.85), transparent 70%),
      radial-gradient(ellipse 420px 200px at 900px 360px, rgba(133,202,230,.55), transparent 70%),
      radial-gradient(ellipse 360px 180px at 140px 380px, rgba(230,103,166,.28), transparent 70%),
      linear-gradient(180deg,#fcf0f6 0%,#f9e2ee 45%,#e3f1f8 100%);}
  .hero-rule{position:absolute;left:0;top:344px;width:843px;height:1px;background:var(--rule)}
  .hero-rule.right{left:1106px;width:94px}

  .site-header{position:absolute;left:0;top:0;width:1200px;height:112px;background:var(--white);border-bottom:3px solid var(--pink)}
  .brand{position:absolute;left:94px;top:14px;width:156px;text-align:center}
  .brand-dot{display:block;width:32px;height:32px;border-radius:50%;background:var(--pink);margin:0 auto 6px}
  .brand-name{display:block;font-size:24px;line-height:24px;font-weight:400;color:var(--plum)}
  .brand-sub{display:block;font-size:9px;letter-spacing:5.5px;margin-top:2px;color:var(--plum)}

  .contact-line{position:absolute;top:17px;right:94px;display:flex;align-items:center;gap:16px;font-family:"Lato",Arial,sans-serif;font-size:15px;color:var(--plum)}
  .contact-item{display:flex;align-items:center;gap:8px}
  .contact-icon{width:26px;height:26px;border-radius:50%;background:var(--pink);display:flex;align-items:center;justify-content:center}

  .main-nav{position:absolute;top:71px;right:94px;display:flex;font-size:13px}
  .main-nav a{color:var(--plum);text-decoration:none;padding:0 19px;border-left:1px solid rgba(230,103,166,.35);line-height:16px;position:relative}
  .main-nav a:first-child{border-left:0}
  .main-nav a:last-child{padding-right:0}
  .main-nav a.active{color:var(--pink)}
  .main-nav a.active::after{content:"";position:absolute;left:50%;top:30px;margin-left:-7px;border:7px solid transparent;border-bottom-color:var(--pink)}

  .headline{position:absolute;left:0;width:856px;top:175px;text-align:center}
  .headline h1{font-family:"Tinos","Times New Roman",serif;font-weight:700;font-size:38px;letter-spacing:.3px;line-height:40px;color:var(--plum)}
  .headline p{font-size:19px;margin-top:6px;color:var(--pink-deep)}

  .service{position:absolute;top:276px;width:200px;text-align:center}
  .service-badge{display:block;margin:0 auto}
  .service h2{font-size:15px;font-weight:400;line-height:20px;margin-top:14px;color:var(--plum)}
  .service-more{display:block;margin:12px auto 0;width:19px;height:19px}

  .contact-panel{position:absolute;left:843px;top:158px;width:263px;height:330px;background:rgba(255,255,255,.92);border:1px solid var(--pink)}
  .contact-panel h3{height:44px;background:var(--pink);color:var(--white);font-family:"Tinos","Times New Roman",serif;font-weight:400;font-size:19px;text-align:center;line-height:44px;position:relative}
  .contact-panel h3::after{content:"";position:absolute;left:50%;bottom:0;margin-left:-8px;border:8px solid transparent;border-bottom:8px solid var(--white);border-top:0}
  .contact-form{padding:15px 15px 0}
  .field{display:block;width:231px;height:33px;background:var(--blush);border:1px solid #f2c6dc;margin-bottom:12px;font-size:11.5px;color:var(--field-text);padding:0 13px;line-height:31px}
  .field.message{height:67px;line-height:normal;padding-top:9px}
  .submit{display:block;width:231px;height:38px;margin-top:13px;background:var(--pink);color:var(--white);border:0;font-family:"Arimo",Arial,sans-serif;font-size:16px;letter-spacing:.3px;border-radius:2px}

  .social-strip{position:absolute;left:1170px;top:225px;width:30px}
  .social-strip a{display:flex;align-items:center;justify-content:center;width:30px;height:30px;color:var(--white);text-decoration:none;font-size:5.5px;letter-spacing:-.1px}
  .s-facenote{background:var(--pink-deep)}
  .s-chatterbox{background:var(--sky)}
  .s-careerweb{background:var(--pink)}
  .s-circleplus{background:var(--sunny);color:var(--plum)!important}
  .get-in-touch{position:absolute;left:1100px;top:356px;width:61px;text-align:right;font-size:11.5px;line-height:15px;color:var(--plum)}
  .touch-arrow{position:absolute;left:1166px;top:358px}

  .site-footer{position:absolute;left:0;top:541px;width:1200px;height:44px;background:var(--pink)}
  .copyright{position:absolute;left:93px;top:15px;font-size:12px;color:var(--white)}
  .footer-brand{position:absolute;right:94px;top:7px;display:flex;align-items:center;gap:8px;color:var(--white)}
  .footer-brand .dot{width:24px;height:24px;border-radius:50%;background:var(--sunny)}
  .footer-brand .name{font-size:18px;line-height:18px}
  .footer-brand .sub{display:block;font-size:7px;letter-spacing:4.5px;margin-top:1px}
</style>
</head>
<body>

<div class="hero-backdrop" role="img" aria-label="Full-width photo of a hand moving a chess piece across a board, in soft pink and sky blue tones"></div>
<div class="hero-rule"></div>
<div class="hero-rule right"></div>

<header class="site-header">
  <div class="brand">
    <span class="brand-dot"></span>
    <span class="brand-name">Maren Holt</span>
    <span class="brand-sub">CONSULTING</span>
  </div>

  <div class="contact-line">
    <span class="contact-item">
      <span class="contact-icon">
        <svg width="13" height="13" viewBox="0 0 24 24"><path fill="#fff" d="M6.6 10.8c1.4 2.8 3.8 5.1 6.6 6.6l2.2-2.2c.3-.3.7-.4 1-.2 1.1.4 2.3.6 3.6.6.6 0 1 .4 1 1V20c0 .6-.4 1-1 1C10.6 21 3 13.4 3 4c0-.6.4-1 1-1h3.5c.6 0 1 .4 1 1 0 1.3.2 2.5.6 3.6.1.3 0 .7-.2 1z"/></svg>
      </span>
      (014) 552-310
    </span>
    <span class="contact-item">
      <span class="contact-icon">
        <svg width="13" height="10" viewBox="0 0 26 20"><rect x="0" y="2" width="26" height="16" fill="#fff"/><path d="M0 2l13 9 13-9" fill="none" stroke="#e667a6" stroke-width="2"/></svg>
      </span>
      info@marenholt.com
    </span>
  </div>

  <nav class="main-nav">
    <a href="#" class="active">Home</a>
    <a href="#">Marketing</a>
    <a href="#">Finance</a>
    <a href="#">Business Key</a>
    <a href="#">Contact Us</a>
  </nav>
</header>

<section class="headline">
  <h1>NOT ALL BUSINESS MAN</h1>
  <p>Can Afford A Few Time Financial Director</p>
</section>

<article class="service" style="left:61px">
  <svg class="service-badge" width="136" height="136" viewBox="0 0 136 136">
    <rect x="21" y="21" width="94" height="94" transform="rotate(45 68 68)" fill="#fff"/>
    <rect x="26" y="26" width="84" height="84" transform="rotate(45 68 68)" fill="#c94b8a"/>
    <rect x="30" y="30" width="76" height="76" transform="rotate(45 68 68)" fill="#e667a6"/>
    <g fill="#fff">
      <circle cx="55" cy="62" r="5"/><path d="M46 78c0-6 4-9 9-9s9 3 9 9z"/>
      <circle cx="81" cy="62" r="5"/><path d="M72 78c0-6 4-9 9-9s9 3 9 9z"/>
      <circle cx="68" cy="64" r="9" fill="none" stroke="#fff" stroke-width="3"/>
      <path d="M74 71l9 9" stroke="#fff" stroke-width="4" stroke-linecap="round"/>
    </g>
  </svg>
  <h2>Business<br>Coach &amp; Mentor</h2>
  <svg class="service-more" viewBox="0 0 19 19"><rect width="19" height="19" fill="#e667a6"/><path d="M9.5 4v11M4 9.5h11" stroke="#fff" stroke-width="3"/></svg>
</article>

<article class="service" style="left:347px">
  <svg class="service-badge" width="136" height="136" viewBox="0 0 136 136">
    <rect x="21" y="21" width="94" height="94" transform="rotate(45 68 68)" fill="#fff"/>
    <rect x="26" y="26" width="84" height="84" transform="rotate(45 68 68)" fill="#85cae6"/>
    <rect x="30" y="30" width="76" height="76" transform="rotate(45 68 68)" fill="#fff"/>
    <g stroke="#e667a6" stroke-linecap="round">
      <path d="M56 56l24 24" stroke-width="5"/>
      <path d="M80 56L58 78" stroke-width="5"/>
      <rect x="76" y="51" width="12" height="7" transform="rotate(45 82 54)" fill="#e667a6" stroke-width="1"/>
      <circle cx="55" cy="55" r="6" fill="none" stroke-width="4"/>
    </g>
  </svg>
  <h2>Rising Finance Rework<br>Restructaring</h2>
  <svg class="service-more" viewBox="0 0 19 19"><rect width="19" height="19" fill="#e667a6"/><path d="M9.5 4v11M4 9.5h11" stroke="#fff" stroke-width="3"/></svg>
</article>

<article class="service" style="left:605px">
  <svg class="service-badge" width="136" height="136" viewBox="0 0 136 136">
    <rect x="21" y="21" width="94" height="94" transform="rotate(45 68 68)" fill="#fff"/>
    <rect x="26" y="26" width="84" height="84" transform="rotate(45 68 68)" fill="#c94b8a"/>
    <rect x="30" y="30" width="76" height="76" transform="rotate(45 68 68)" fill="#e667a6"/>
    <g fill="#fff">
      <circle cx="66" cy="55" r="6"/>
      <path d="M54 76c0-9 5-13 12-13s12 4 12 13z"/>
      <path d="M52 83l14-10 8 5 10-8-2-3h8v8l-3-2-13 11-8-5-12 8z" fill="#fbee3e"/>
    </g>
  </svg>
  <h2>Taking Your Business<br>To The Next Leval</h2>
  <svg class="service-more" viewBox="0 0 19 19"><rect width="19" height="19" fill="#e667a6"/><path d="M9.5 4v11M4 9.5h11" stroke="#fff" stroke-width="3"/></svg>
</article>

<aside class="contact-panel">
  <h3>Contact Now</h3>
  <form class="contact-form">
    <div class="field">Your Name</div>
    <div class="field">Email Address</div>
    <div class="field">Phone</div>
    <div class="field message">Message</div>
    <button class="submit" type="button">SUBMIT</button>
  </form>
</aside>

<nav class="social-strip" aria-label="Social links">
  <a class="s-facenote" href="#">facenote</a>
  <a class="s-chatterbox" href="#">chatterbox</a>
  <a class="s-careerweb" href="#">careerweb</a>
  <a class="s-circleplus" href="#">circleplus</a>
</nav>

<div class="get-in-touch">Get<br>In Touch</div>
<svg class="touch-arrow" width="34" height="28" viewBox="0 0 34 28">
  <path d="M34 4C24 6 12 10 2 14c10 3 22 7 32 10" fill="none" stroke="#e667a6" stroke-width="1.3"/>
  <path d="M34 14H12" stroke="#e667a6" stroke-width="1.3"/>
</svg>

<footer class="site-footer">
  <p class="copyright">Copyright 2016 Maren Holt . All rights reserved.</p>
  <div class="footer-brand">
    <span class="dot"></span>
    <span class="name">Maren Holt<span class="sub">CONSULTING</span></span>
  </div>
</footer>

</body>
</html>
```